Stock certificate

We need a stock certificate with a modern design aligned with our company background (Consulting & IT-Services Company with innovation drive).
The certificate should include our logo and should have some space to insert our dedicated text (value, issuer, etc.).
Format should be A4 landscape. The page must be workable, meaning that the background of the certificate can be fixed (kind of master), but the front where the text shall be written must be flexible. PPT-format could make it for example.
Velto font style desired.
Required text areas are shown in the uploaded example.
Velto font style would be great.
It Company

```html
<!DOCTYPE html>
<html lang="en">
<head>
<meta charset="utf-8">
<title>Aktienzertifikat – Quantora</title>
<link rel="stylesheet" href="https://fonts.googleapis.com/css2?family=Open+Sans:wght@300&family=Carlito:wght@400&display=swap">
<style>
  :root {
    --paper: #f4f8fc;
    --ink: #1d2b45;
    --ink-soft: #2a3a55;
    --title: #8fa9c4;
    --title-deep: #3d5f86;
    --rule: #9cb4cf;
    --wave-light: #cfe3f3;
  }
  * { margin: 0; padding: 0; box-sizing: border-box; }
  html, body { width: 1200px; height: 900px; overflow: hidden; background: var(--paper); }
  .certificate {
    position: relative;
    width: 1200px;
    height: 900px;
    overflow: hidden;
    font-family: "Carlito", "Calibri", sans-serif;
    color: var(--ink);
    background: var(--paper);
  }
  .certificate__artwork {
    position: absolute;
    inset: 0;
    background:
      radial-gradient(ellipse 520px 240px at 620px 330px, rgba(47,143,208,0.55), transparent 70%),
      radial-gradient(ellipse 380px 320px at 140px 560px, rgba(47,143,208,0.45), transparent 70%),
      radial-gradient(ellipse 300px 220px at 1050px 470px, rgba(47,143,208,0.35), transparent 70%),
      radial-gradient(ellipse 260px 260px at 1030px 130px, rgba(120,140,165,0.30), transparent 70%),
      linear-gradient(160deg, #eef4fa 0%, var(--wave-light) 40%, #f2f7fb 70%, #ffffff 100%);
  }
  .certificate__title {
    position: absolute;
    left: 180px;
    top: 14px;
    font-family: "Open Sans", "Helvetica Neue", sans-serif;
    font-weight: 300;
    font-size: 124px;
    line-height: 1.2;
    letter-spacing: -2px;
    white-space: nowrap;
    background: linear-gradient(90deg, var(--title) 0%, var(--title) 22%, var(--title-deep) 35%, var(--title-deep) 60%, #1c2c44 66%, var(--title) 80%, var(--title) 100%);
    -webkit-background-clip: text;
    background-clip: text;
    color: transparent;
  }
  .certificate__intro {
    position: absolute;
    left: 77px;
    top: 226px;
    width: 395px;
  }
  .certificate__label { font-size: 20px; line-height: 24px; color: var(--ink-soft); }
  .certificate__body {
    margin-top: 8px;
    font-size: 16.2px;
    line-height: 20.1px;
    color: var(--ink);
  }
  .certificate__fields {
    position: absolute;
    left: 638px;
    top: 0;
    width: 460px;
    height: 600px;
    list-style: none;
  }
  .field {
    position: absolute;
    left: 0;
    width: 460px;
    height: 24px;
    font-size: 20px;
    line-height: 22px;
    color: var(--ink-soft);
    border-bottom: 1.5px solid var(--rule);
  }
  .field--number { top: 228px; }
  .field--holder { top: 310px; }
  .field--registered { top: 391px; }
  .field--place { top: 480px; }
  .field--company { top: 570px; }
  .certificate__mark {
    position: absolute;
    left: 806px;
    top: 640px;
    font-family: "Carlito", "Calibri", sans-serif;
    font-weight: 400;
    font-size: 64px;
    line-height: 1;
    color: var(--ink-soft);
  }
  .signature {
    position: absolute;
    top: 780px;
    width: 283px;
    font-size: 20px;
    line-height: 24px;
    color: var(--ink-soft);
  }
  .signature--first { left: 77px; }
  .signature--second { left: 456px; }
  .signature--third { left: 815px; }
  .signature__name { border-bottom: 1.5px solid var(--rule); padding-bottom: 14px; }
  .signature__role { margin-top: 5px; }
</style>
</head>
<body>
<main class="certificate">
  <div class="certificate__artwork" role="img" aria-label="Abstract flowing blue light waves with fine grey guilloche line patterns across the background"></div>

  <h1 class="certificate__title">AKTIENZERTIFIKAT</h1>

  <section class="certificate__intro">
    <p class="certificate__label">Company</p>
    <p class="certificate__body">Lorem ipsum dolor sit amet, consectetur adipiscing elit. Donec scelerisque ligula mi, ac consequat risus iaculis et. Vivamus ullamcorper mauris auctor semper commodo. Integer volutpat massa eget sapien placerat fringilla. Curabitur eu volutpat tortor. Ut viverra dolor sapien, sed hendrerit ipsum ultricies eu. Pellentesque condimentum scelerisque velit at viverra. Sed auctor pulvinar eros ut sollicitudin. Donec posuere eget turpis congue tempus. Nulla facilisis, augue non eleifend ultrices, nibh leo lacinia elit, eget ultricies leo arcu quis lacus. Praesent laoreet vehicula massa pulvinar tincidunt. Curabitur sagittis, lorem sit amet sollicitudin mattis, est mi scelerisque sapien, et tempus purus arcu non urna. Fusce sollicitudin odio nec adipiscing aliquet. Nullam rhoncus lorem non commodo egestas. Morbi sit amet tincidunt turpis. Nullam a sapien luctus, vulputate metus ut, gravida velit.</p>
  </section>

  <ul class="certificate__fields">
    <li class="field field--number">No of certificate: 00000000</li>
    <li class="field field--holder">The shareholder Mr A. N. Other, persons title</li>
    <li class="field field--registered">Registered:&nbsp; 00000000</li>
    <li class="field field--place">Location, date</li>
    <li class="field field--company">Company</li>
  </ul>

  <p class="certificate__mark">Quantora</p>

  <footer class="signatures">
    <div class="signature signature--first"><p class="signature__name">Name</p><p class="signature__role">Member of the board</p></div>
    <div class="signature signature--second"><p class="signature__name">Name</p><p class="signature__role">Member of the board</p></div>
    <div class="signature signature--third"><p class="signature__name">Name</p><p class="signature__role">Member of the board</p></div>
  </footer>
</main>
</body>
</html>
```